Northfield Builders Guild Business card

We are looking for a new business card design with photo included.
Our business is a nonprofit construction contractor membership organization. We offer business education, assist with business setup and licensing, provide safety training, and provide a member directory.
URL: www.brickwayguildnetwork.org
Color code:
CMYK: 0 cyan, 42 magenta, 100 yellow, 0 black for Print.
Hexidecimal: #FF9900
RGB: R 255; G 153; B 0

```html
<!DOCTYPE html>
<html lang="en">
<head>
<meta charset="utf-8">
<title>Northfield Builders Guild – Business Card</title>
<link href="https://fonts.googleapis.com/css2?family=Source+Sans+3:wght@400;600;700;800&display=swap" rel="stylesheet">
<style>
  :root {
    --orange: #f4a51c;
    --charcoal: #444344;
    --charcoal-deep: #363536;
    --paper: #f7f7f7;
    --ink: #3a393a;
    --muted: #d9d9d9;
    --backdrop: #cfcfcf;
  }
  * { margin: 0; padding: 0; box-sizing: border-box; }
  html, body {
    width: 1200px; height: 800px; overflow: hidden;
    background: var(--backdrop);
    font-family: "Source Sans 3", Arial, sans-serif;
  }
  .canvas { position: relative; width: 1200px; height: 800px; }

  .card {
    position: absolute; width: 560px; height: 320px;
    box-shadow: 0 6px 18px rgba(0,0,0,0.18);
    overflow: hidden;
  }

  /* Front */
  .card-front { left: 70px; top: 70px; background: var(--charcoal); }
  .brand {
    display: flex; align-items: center; gap: 12px;
    font-weight: 800; text-transform: uppercase; letter-spacing: 0.5px;
    line-height: 1;
  }
  .brand-mark { width: 14px; height: 14px; background: var(--orange); flex: none; }
  .card-front .brand {
    position: absolute; left: 0; right: 0; top: 92px;
    justify-content: center; color: #ffffff; font-size: 34px;
  }
  .front-rule {
    position: absolute; left: 255px; top: 160px;
    width: 50px; height: 2px; background: var(--orange);
  }
  .services {
    position: absolute; left: 0; right: 0; top: 196px;
    text-align: center; color: var(--muted);
    font-size: 15px; letter-spacing: 0.3px; line-height: 1.45;
    text-transform: uppercase;
  }
  .services .dot { color: var(--orange); font-weight: 700; padding: 0 4px; }

  /* Back */
  .card-back { left: 570px; top: 410px; background: var(--paper); }
  .card-back .brand {
    position: absolute; left: 36px; top: 108px;
    color: var(--ink); font-size: 24px;
  }
  .holder {
    position: absolute; right: 36px; top: 88px; text-align: right;
  }
  .holder-name { color: var(--orange); font-weight: 700; font-size: 22px; line-height: 1.1; }
  .holder-title { color: var(--ink); font-size: 15px; margin-top: 2px; }
  .back-rule {
    position: absolute; left: 36px; right: 36px; top: 158px;
    height: 2px; background: var(--orange);
  }
  .contacts {
    position: absolute; left: 40px; top: 184px; list-style: none;
    color: var(--ink); font-size: 14.5px; line-height: 1.45;
  }
  .contacts li { display: flex; align-items: center; gap: 8px; }
  .contacts svg { width: 13px; height: 13px; flex: none; }
  .address {
    position: absolute; right: 36px; top: 184px; text-align: right;
    font-style: normal; color: var(--ink); font-size: 14.5px; line-height: 1.45;
  }
  .edge-band { position: absolute; left: 0; bottom: 0; width: 100%; height: 14px; }
</style>
</head>
<body>
<main class="canvas">

  <section class="card card-front" aria-label="Card front">
    <div class="brand"><span class="brand-mark"></span>Northfield Builders Guild</div>
    <div class="front-rule"></div>
    <p class="services">
      Technical Assistance<span class="dot">•</span>Contractor Education<br>
      Safety &amp; Compliance<span class="dot">•</span>Contractor Directory
    </p>
  </section>

  <section class="card card-back" aria-label="Card back">
    <div class="brand"><span class="brand-mark"></span>Northfield Builders Guild</div>

    <div class="holder">
      <div class="holder-name">Daniel Harper</div>
      <div class="holder-title">President</div>
    </div>

    <div class="back-rule"></div>

    <ul class="contacts">
      <li>
        <svg viewBox="0 0 16 16" aria-hidden="true"><path fill="var(--orange)" d="M3.6 1.5l2.3 2.6-1.3 1.7c.9 2 2.4 3.6 4.6 4.6l1.7-1.3 2.6 2.3-1.4 2.4C6.7 13.9 2.1 9.3 1.2 3z"/></svg>
        (555) 318-2047
      </li>
      <li>
        <svg viewBox="0 0 16 16" aria-hidden="true"><rect x="4" y="1.5" width="8" height="5" fill="none" stroke="var(--orange)" stroke-width="1.5"/><rect x="1.5" y="6" width="13" height="8" rx="1" fill="var(--orange)"/></svg>
        555.274.6631
      </li>
      <li>
        <svg viewBox="0 0 16 16" aria-hidden="true"><rect x="1.5" y="3.5" width="13" height="9" fill="none" stroke="var(--orange)" stroke-width="1.5"/><path d="M1.5 3.5l6.5 5 6.5-5" fill="none" stroke="var(--orange)" stroke-width="1.5"/></svg>
        daniel@brickwayguildnetwork.org
      </li>
      <li>
        <svg viewBox="0 0 16 16" aria-hidden="true"><g fill="none" stroke="var(--orange)" stroke-width="1.3"><circle cx="8" cy="8" r="6.3"/><ellipse cx="8" cy="8" rx="2.8" ry="6.3"/><path d="M1.7 8h12.6M2.8 4.8h10.4M2.8 11.2h10.4"/></g></svg>
        www.brickwayguildnetwork.org
      </li>
    </ul>

    <address class="address">
      4200 Alder Ridge Rd.<br>
      Suite #210<br>
      Fairhaven, OR 97000
    </address>

    <svg class="edge-band" viewBox="0 0 560 14" preserveAspectRatio="none" aria-hidden="true">
      <polygon points="0,0 360,0 352,14 0,14" fill="var(--charcoal-deep)"/>
      <polygon points="366,0 560,0 560,14 358,14" fill="var(--orange)"/>
    </svg>
  </section>

</main>
</body>
</html>
```